Q-Rolls Business Card

We are a modern retail clothing store. Established in 1994. I need a presentable card that will amaze vendors when given to them.

Front: Logo in middle
Info Side:

Name: Tomas Velder
Cell: 630-812-4463
Work: 630-917-3384 EXT. 417
Email: Tomas@q-rolls-example.com
Website: www.Q-rolls-example.com

Industry/Entity Type

Business

```html
<!DOCTYPE html>
<html lang="en">
<head>
<meta charset="utf-8">
<title>Q-Rolls Business Card</title>
<link href="https://fonts.googleapis.com/css2?family=Bebas+Neue&family=Open+Sans:wght@400&display=swap" rel="stylesheet">
<style>
  :root {
    --backdrop: #e6e2dd;
    --card-light: #ffffff;
    --card-dark: #232323;
    --ink: #111111;
    --logo-gloss: #121212;
    --rule: #1a1a1a;
  }
  * { margin: 0; padding: 0; box-sizing: border-box; }
  html, body {
    width: 1200px;
    height: 1000px;
    overflow: hidden;
    background: var(--backdrop);
  }
  .canvas {
    position: relative;
    width: 1200px;
    height: 1000px;
  }
  .card {
    position: absolute;
    left: 266px;
    width: 665px;
    height: 397px;
    border-radius: 28px;
  }
  .card--info {
    top: 73px;
    background: var(--card-light);
    box-shadow: 0 6px 14px rgba(0,0,0,0.25);
  }
  .card--logo {
    top: 533px;
    height: 395px;
    background: var(--card-dark);
    box-shadow: 0 6px 14px rgba(0,0,0,0.3);
  }
  .identity {
    position: absolute;
    right: 353px;
    top: 168px;
    text-align: right;
    color: var(--ink);
  }
  .identity__name {
    font-family: "Bebas Neue", sans-serif;
    font-size: 44px;
    line-height: 40px;
    letter-spacing: 0.5px;
  }
  .identity__title {
    font-family: "Open Sans", sans-serif;
    font-size: 15px;
    line-height: 20px;
    margin-top: 4px;
  }
  .divider {
    position: absolute;
    left: 331px;
    top: 160px;
    width: 2px;
    height: 78px;
    background: var(--rule);
  }
  .contacts {
    position: absolute;
    left: 350px;
    top: 155px;
    list-style: none;
    font-family: "Open Sans", sans-serif;
    font-size: 15.5px;
    color: var(--ink);
  }
  .contacts__item {
    display: flex;
    align-items: center;
    height: 22.3px;
  }
  .contacts__icon {
    width: 14px;
    height: 14px;
    margin-right: 8px;
    fill: var(--ink);
  }
  .brand-name {
    position: absolute;
    left: 0;
    right: 0;
    top: 140px;
    text-align: center;
    font-family: "Bebas Neue", sans-serif;
    font-size: 120px;
    line-height: 120px;
    letter-spacing: 4px;
    color: var(--logo-gloss);
  }
</style>
</head>
<body>
<main class="canvas">
  <section class="card card--info">
    <div class="identity">
      <div class="identity__name">TOMAS VELDER</div>
      <div class="identity__title">President</div>
    </div>
    <div class="divider"></div>
    <ul class="contacts">
      <li class="contacts__item">
        <svg class="contacts__icon" viewBox="0 0 14 14" aria-hidden="true"><path d="M4 0h1v2h4a1 1 0 0 1 1 1v10a1 1 0 0 1-1 1H5a1 1 0 0 1-1-1zM5.5 3.5v3h3v-3z"/></svg>
        630-812-4463
      </li>
      <li class="contacts__item">
        <svg class="contacts__icon" viewBox="0 0 14 14" aria-hidden="true"><path d="M1 4c0-2 3-3 6-3s6 1 6 3v1h-3V4H4v1H1zM3 6h8l2 6H1z"/></svg>
        630-917-3384 EXT. 417
      </li>
      <li class="contacts__item">
        <svg class="contacts__icon" viewBox="0 0 14 14" aria-hidden="true"><path d="M0 3h14v1L7 8 0 4zM0 5.5l7 4 7-4V11H0z"/></svg>
        Tomas@q-rolls-example.com
      </li>
      <li class="contacts__item">
        <svg class="contacts__icon" viewBox="0 0 14 14" aria-hidden="true"><path d="M7 0a7 7 0 1 0 0 14A7 7 0 0 0 7 0zm0 2a5 5 0 0 1 4.6 3H9L7 3zM2.4 5H5L4 8l2 2v2A5 5 0 0 1 2.4 5z"/></svg>
        www.Q-rolls-example.com
      </li>
    </ul>
  </section>

  <section class="card card--logo">
    <div class="brand-name">Q-ROLLS</div>
  </section>
</main>
</body>
</html>
```